Rolf Denning & Martin Oakshaw Two Piano Recital

We need a flyer designed to advertise a classical concert featuring pianists Martin Oakshaw & Rolf Denning playing two pianos.

The concert will be held at Brindlemoor College on Thursday, June 12th at 7:30pm
Supper will be served!
We need something that will get noticed and look cool possibly using the photo attached?

```html
<!DOCTYPE html>
<html lang="en">
<head>
<meta charset="utf-8">
<title>Rolf Denning &amp; Martin Oakshaw – Two Piano Recital</title>
<link rel="stylesheet" href="https://fonts.googleapis.com/css2?family=Oswald:wght@400;500&display=swap">
<style>
  :root {
    --backdrop: #e4e4e4;
    --ink: #222222;
    --charcoal: #2e2e2e;
    --accent-yellow: #f7ea1c;
    --paper-white: #ffffff;
    --photo-light: #d2d2d2;
    --photo-mid: #8f8f8f;
    --photo-dark: #3c3c3c;
    --keys-light: rgba(235, 235, 235, 0.82);
    --keys-dark: rgba(40, 40, 40, 0.55);
  }
  * { margin: 0; padding: 0; box-sizing: border-box; }
  html, body {
    width: 1200px;
    height: 819px;
    overflow: hidden;
    background: var(--backdrop);
    font-family: "Oswald", "Arial Narrow", sans-serif;
  }
  .canvas {
    position: relative;
    width: 1200px;
    height: 819px;
  }
  .flyer {
    position: absolute;
    left: 365px;
    top: 70px;
    width: 470px;
    height: 680px;
    background: var(--charcoal);
    overflow: hidden;
    box-shadow: 0 6px 18px rgba(0, 0, 0, 0.25);
  }
  .flyer__top-band {
    position: absolute;
    left: 0; top: 0;
    width: 100%;
    height: 14px;
    background: var(--charcoal);
  }
  .flyer__photo {
    position: absolute;
    left: 0; top: 14px;
    width: 100%;
    height: 650px;
    background:
      linear-gradient(90deg, rgba(40,40,40,0.55) 0%, rgba(255,255,255,0) 30%, rgba(255,255,255,0) 55%, rgba(40,40,40,0.6) 80%, rgba(40,40,40,0.3) 100%),
      linear-gradient(180deg, var(--photo-light) 0%, var(--photo-mid) 55%, var(--photo-dark) 100%);
  }
  .keyboard-band {
    position: absolute;
    height: 78px;
    background: linear-gradient(180deg, var(--keys-dark) 0%, var(--keys-dark) 55%, var(--keys-light) 55%, var(--keys-light) 100%);
    transform-origin: left center;
  }
  .keyboard-band--diagonal {
    left: -20px;
    top: 395px;
    width: 480px;
    transform: rotate(38deg);
  }
  .keyboard-band--rising {
    left: -20px;
    top: 560px;
    width: 540px;
    transform: rotate(-13deg);
  }
  .flyer__bottom-band {
    position: absolute;
    left: 0; bottom: 0;
    width: 100%;
    height: 16px;
    background: var(--accent-yellow);
  }
  .headline {
    position: absolute;
    left: 0;
    top: 100px;
  }
  .headline__line {
    display: block;
    width: max-content;
    background: var(--accent-yellow);
    color: var(--ink);
    font-weight: 500;
    font-size: 29px;
    line-height: 42px;
    padding: 0 20px 0 24px;
    margin-bottom: 6px;
  }
  .event-details {
    position: absolute;
    left: 0;
    top: 228px;
  }
  .event-details__line {
    display: block;
    width: max-content;
    background: var(--charcoal);
    color: var(--paper-white);
    font-size: 22px;
    line-height: 40px;
    padding: 0 16px 0 24px;
    margin-bottom: 2px;
  }
  .supper-badge {
    position: absolute;
    left: 262px;
    top: 430px;
    width: 124px;
    height: 124px;
    border-radius: 50%;
    background: var(--charcoal);
    border: 4px solid var(--accent-yellow);
    color: var(--paper-white);
    display: flex;
    align-items: center;
    justify-content: center;
    text-align: center;
    font-weight: 500;
    font-size: 18px;
    line-height: 24px;
    text-transform: uppercase;
  }
</style>
</head>
<body>
<main class="canvas">
  <article class="flyer">
    <div class="flyer__top-band"></div>
    <div class="flyer__photo" role="img" aria-label="Black and white photo of two pianists in waistcoats standing side by side"></div>
    <div class="keyboard-band keyboard-band--diagonal" role="img" aria-label="Piano keyboard strip crossing the photo diagonally"></div>
    <div class="keyboard-band keyboard-band--rising" role="img" aria-label="Piano keyboard strip rising across the lower photo"></div>

    <h1 class="headline">
      <span class="headline__line">Martin Oakshaw &amp; Rolf Denning</span>
      <span class="headline__line">playing two pianos</span>
    </h1>

    <p class="event-details">
      <span class="event-details__line">Brindlemoor College on Thursday,</span>
      <span class="event-details__line">June 12th at 7:30pm</span>
    </p>

    <div class="supper-badge">Supper<br>will be<br>served!</div>

    <div class="flyer__bottom-band"></div>
  </article>
</main>
</body>
</html>
```